Modern and appealing business Wordpress site

I've been operating my consulting firm for 5 years and feel like it is time to really improve on my web presence as I'm starting to get more national attention. I had a logo made through this service a couple of years ago, and would like to get a website that matches the look of it. The website will be used to (1) advertise my services (2) provide a brief overview of our management philosophies, and (3) host a resource library database. I understand HTML, but am not as familiar with how to code Wordpress, so I need someone that can help upload themes.

The website can be found at www.trelmondgroup.com.

For design, I prefer round designs to square and want the color scheme to match the attached logo. I have included both the full logo and the abbreviated one.

I also have a new picture for CFO uploaded. I plan on getting a new one for the CEO in the coming weeks, so I would like someone that I could get to help make the modification at a later time.

The resource database will be put into a document library (probably Kiln7) once the final design is completed rather than having multiple pages with links...just so you know the final vision for the site.

Reach out if you have any questions.

Target Market(s)

Community Action Agencies, Nonprofit Organization Leaders

Industry/Entity Type

Consulting

Coding

Coded - Design and coding required

Font styles to use
Sans Serif

Requirements
Must have
• Must match the color scheme of the attached logo

```html
<!DOCTYPE html>
<html lang="en">
<head>
<meta charset="utf-8">
<title>Trelmond LLC</title>
<link href="https://fonts.googleapis.com/css2?family=Lato:wght@400;700;900&family=Open+Sans:wght@400;600&display=swap" rel="stylesheet">
<style>
:root{
  --blue:#1e9ad6;
  --blue-dark:#137cb3;
  --navy:#0c2a45;
  --navy-deep:#071a2c;
  --ink:#2b2f36;
  --muted:#6b7480;
  --light:#f2f4f7;
  --white:#ffffff;
}
*{box-sizing:border-box;margin:0;padding:0}
html,body{width:1200px;height:3136px;overflow:hidden;background:var(--white)}
body{font-family:"Open Sans",Arial,sans-serif;color:var(--ink);font-size:14px;line-height:1.6}
h1,h2,h3,h4,.brand,.nav,.btn{font-family:"Lato",Arial,sans-serif}
.wrap{width:1040px;margin:0 auto;position:relative}

.topbar{height:36px;background:var(--blue);color:var(--white);font-size:12px}
.topbar .wrap{display:flex;justify-content:space-between;align-items:center;height:36px}
.topbar .contact{display:flex;gap:26px;align-items:center}
.topbar .contact span{display:flex;gap:6px;align-items:center}
.social{display:flex;gap:8px}
.social i{width:18px;height:18px;border-radius:50%;background:rgba(255,255,255,.35);display:block}

.header{height:90px;background:var(--white);box-shadow:0 2px 6px rgba(0,0,0,.06);position:relative;z-index:2}
.header .wrap{display:flex;justify-content:space-between;align-items:center;height:90px}
.brand{display:flex;align-items:center;gap:10px;font-size:30px;font-weight:900;color:var(--navy);letter-spacing:1px}
.brand .dot{width:34px;height:34px;border-radius:50%;background:var(--blue)}
.nav{display:flex;gap:30px;align-items:center;font-size:12px;font-weight:700;color:var(--navy);letter-spacing:.5px}
.nav .active{color:var(--blue);border-bottom:2px solid var(--blue);padding-bottom:4px}
.btn{display:inline-block;font-size:11px;font-weight:700;letter-spacing:1px;padding:9px 22px;border-radius:20px;text-transform:uppercase}
.btn-fill{background:var(--blue);color:var(--white)}
.btn-line{border:1px solid var(--blue);color:var(--blue)}
.btn-white{border:1px solid rgba(255,255,255,.8);color:var(--white)}

.hero{height:540px;position:relative;background:radial-gradient(ellipse at 75% 55%,#2f7fc0 0%,#123e6e 40%,#061a33 100%);color:var(--white);text-align:center;overflow:hidden}
.hero .copy{position:absolute;top:120px;left:0;right:0}
.hero .eyebrow{display:inline-block;font-size:13px;background:rgba(30,154,214,.55);padding:4px 14px;border-radius:14px;margin-bottom:14px}
.hero h1{font-size:40px;font-weight:900;line-height:1.25;margin-bottom:26px}
.dots{display:flex;gap:8px;justify-content:center}
.dots i{width:9px;height:9px;border-radius:50%;background:#bfc7cf;display:block}
.dots i.on{background:var(--blue)}
.hero .dots{position:absolute;bottom:24px;left:0;right:0}
.hero .dots i{background:rgba(255,255,255,.5)}
.hero .dots i.on{background:var(--white)}

.about{height:500px;padding-top:90px}
.about .wrap{display:flex;gap:60px}
.about .photo{width:420px;height:300px;border-radius:4px;background:linear-gradient(135deg,#1c4f7e,#4b86b8 60%,#c9d6e2);position:relative;flex:none}
.badge{position:absolute;right:-16px;bottom:-20px;width:110px;height:110px;background:var(--blue);color:var(--white);text-align:center;padding-top:20px;border-radius:6px}
.badge strong{display:block;font-family:"Lato",sans-serif;font-size:40px;font-weight:900;line-height:1}
.badge span{font-size:12px;font-weight:700;letter-spacing:1px}
.about h2{font-size:26px;font-weight:900;color:var(--blue);line-height:1.25;margin:20px 0 18px}
.about p{color:var(--muted);font-size:13px;margin-bottom:14px}

.services{height:620px;background:linear-gradient(180deg,#0d3152,#071a2c);color:var(--white);text-align:center;padding-top:70px}
.section-title{font-size:28px;font-weight:900;letter-spacing:1px}
.rule{width:50px;height:3px;background:var(--blue);margin:12px auto 40px}
.cards{display:flex;gap:30px;justify-content:center}
.card{width:320px}
.card .img{height:200px}
.card .body{background:var(--blue);padding:18px 22px 22px;text-align:left;height:110px}
.card.alt .body{background:#55606b}
.card h3{font-size:17px;font-weight:700;margin-bottom:4px}
.card p{font-size:12px;opacity:.85}
.services .btn{margin-top:44px}

.testimonials{height:520px;background:var(--light);text-align:center;padding-top:70px}
.testimonials .section-title{color:var(--navy)}
.quotes{display:flex;gap:40px;justify-content:center}
.quote{width:480px}
.quote .box{background:var(--blue);color:var(--white);padding:26px 34px;height:190px;font-size:13px}
.quote .mark{font-family:"Lato",sans-serif;font-size:46px;font-weight:900;line-height:.8;display:block;margin-bottom:8px}
.quote cite{display:block;font-style:normal;font-weight:700;font-size:13px;color:var(--navy);margin-top:14px}
.testimonials .dots{margin-top:34px}

.mission{height:480px;background:linear-gradient(90deg,#e8edf2,#ffffff 60%);padding-top:90px}
.mission .wrap{display:flex;justify-content:space-between}
.mission .text{width:420px;padding-top:30px}
.mission h2{font-size:28px;font-weight:900;color:var(--blue)}
.mission .rule{margin:10px 0 20px}
.mission p{color:var(--muted);font-size:13px}
.team{display:flex;gap:30px}
.member{width:230px;text-align:center}
.member .img{height:230px;border-radius:4px}
.member strong{display:block;color:var(--blue);font-size:14px;margin-top:12px;font-family:"Lato",sans-serif}
.member span{font-size:12px;color:var(--muted)}

.footer{height:350px;background:var(--navy-deep);color:#c7d1db;position:relative}
.footer .wrap{display:flex;gap:90px;padding-top:60px}
.footer h4{color:var(--white);font-size:16px;font-weight:700;margin-bottom:6px}
.footer .rule{margin:0 0 18px}
.footer ul{list-style:none;font-size:13px;line-height:2}
.footer .info li{display:flex;gap:10px;align-items:center}
.form{width:420px;display:grid;grid-template-columns:1fr 1fr;gap:12px}
.form i{display:block;height:34px;border:1px solid #2a4661;border-radius:3px}
.form i.wide{grid-column:1/3;height:70px}
.form .btn{justify-self:start}
.copyright{position:absolute;left:0;right:0;bottom:0;height:40px;background:var(--blue);color:var(--white);font-size:12px}
.copyright .wrap{display:flex;justify-content:space-between;align-items:center;height:40px;padding:0}
</style>
</head>
<body>

<div class="topbar">
  <div class="wrap">
    <div class="contact">
      <span><svg width="14" height="10" viewBox="0 0 14 10"><rect x=".5" y=".5" width="13" height="9" fill="none" stroke="#fff"/><path d="M.5 .5 7 6l6.5-5.5" fill="none" stroke="#fff"/></svg>info@trelmondgroup.com</span>
      <span><svg width="12" height="12" viewBox="0 0 12 12"><path d="M2 1h2.5l1 3-1.5 1a7 7 0 0 0 3 3l1-1.5 3 1V10a1 1 0 0 1-1 1A9 9 0 0 1 1 2a1 1 0 0 1 1-1z" fill="#fff"/></svg>(555) 014-2270</span>
    </div>
    <div class="social"><i></i><i></i><i></i><i></i></div>
  </div>
</div>

<header class="header">
  <div class="wrap">
    <div class="brand"><span class="dot"></span>TRELMOND</div>
    <nav class="nav">
      <span class="active">HOME</span><span>SERVICES</span><span>BLOG</span><span>LINKS</span><span>RESOURCES</span><span>CONTACT</span>
      <span class="btn btn-fill">Get a Quote</span>
    </nav>
  </div>
</header>

<section class="hero" role="img" aria-label="Hand touching a glowing digital network interface on a dark blue background">
  <div class="copy">
    <div class="eyebrow">Welcome To Trelmond LLC</div>
    <h1>Lorem Ipsum is simply dummy text<br>of the printing industry.</h1>
    <span class="btn btn-fill">Read More</span>
  </div>
  <div class="dots"><i class="on"></i><i></i><i></i></div>
</section>

<section class="about">
  <div class="wrap">
    <div class="photo" role="img" aria-label="Business colleagues reviewing a tablet together">
      <div class="badge"><strong>20</strong><span>YEARS</span></div>
    </div>
    <div class="text">
      <h2>LEADING ORGANIZATIONS TO<br>EXCELLENCE!</h2>
      <p>Trelmond LLC was created to help nonprofits and community action agencies build stronger systems, sharpen strategy and grow the leaders who move their mission forward every single day.</p>
      <p>Our approach is rooted in clear planning, honest data and practical coaching, so every team we serve can measure progress, tell its story well and reach lasting results.</p>
      <span class="btn btn-line">Read More</span>
    </div>
  </div>
</section>

<section class="services">
  <h2 class="section-title">OUR SERVICES</h2>
  <div class="rule"></div>
  <div class="cards">
    <div class="card">
      <div class="img" role="img" aria-label="Team meeting around a table" style="background:linear-gradient(135deg,#7d8c99,#c7cfd6)"></div>
      <div class="body"><h3>Training &amp; Consulting</h3><p>Hands-on training and guidance that help your staff plan, lead and deliver.</p></div>
    </div>
    <div class="card">
      <div class="img" role="img" aria-label="Glowing data charts on a dark screen" style="background:linear-gradient(135deg,#0b3a66,#2d8fd0)"></div>
      <div class="body"><h3>Data Analytics</h3><p>Clear reporting and analysis that turn your numbers into better decisions.</p></div>
    </div>
    <div class="card alt">
      <div class="img" role="img" aria-label="Vintage typewriter on a desk" style="background:linear-gradient(135deg,#3c4046,#9aa0a6)"></div>
      <div class="body"><h3>Storytelling</h3><p>Compelling reports and narratives that show the impact of your work.</p></div>
    </div>
  </div>
  <span class="btn btn-white">View All</span>
</section>

<section class="testimonials">
  <h2 class="section-title">TESTIMONIALS</h2>
  <div class="rule"></div>
  <div class="quotes">
    <div class="quote">
      <div class="box"><span class="mark">&ldquo;</span>The training our team received was clear, practical and easy to apply. Our managers left with real tools, and we have seen stronger planning and better results across every program since.</div>
      <cite>Riverbend Senior Services</cite>
    </div>
    <div class="quote">
      <div class="box"><span class="mark">&ldquo;</span>Working with this team helped us organize our data and tell our story with confidence. Our board and funders now see the true value of our work, and we could not be more pleased.</div>
      <cite>Community Action Partnership of Lakeshore</cite>
    </div>
  </div>
  <div class="dots"><i class="on"></i><i></i><i></i></div>
</section>

<section class="mission">
  <div class="wrap">
    <div class="text">
      <h2>OUR MISSION</h2>
      <div class="rule"></div>
      <p>To help community action organizations, nonprofit leaders and their teams achieve excellence through clear strategy, reliable data and strong, lasting leadership in the communities they serve.</p>
    </div>
    <div class="team">
      <div class="member">
        <div class="img" role="img" aria-label="Portrait photo of the CEO" style="background:linear-gradient(160deg,#5a7fa3,#2a3f57)"></div>
        <strong>Dana Whitfield</strong><span>Chief Executive Officer</span>
      </div>
      <div class="member">
        <div class="img" role="img" aria-label="Portrait photo of the CFO" style="background:linear-gradient(160deg,#7fae7a,#3d6a4a)"></div>
        <strong>Marisa Oakley</strong><span>Chief Financial Officer</span>
      </div>
    </div>
  </div>
</section>

<footer class="footer">
  <div class="wrap">
    <div>
      <h4>Quick Links</h4><div class="rule"></div>
      <ul><li>Home</li><li>Services</li><li>Blog</li><li>Links</li><li>Resources</li><li>Contact</li></ul>
    </div>
    <div>
      <h4>Contact Info</h4><div class="rule"></div>
      <ul class="info">
        <li><svg width="12" height="12" viewBox="0 0 12 12"><path d="M2 1h2.5l1 3-1.5 1a7 7 0 0 0 3 3l1-1.5 3 1V10a1 1 0 0 1-1 1A9 9 0 0 1 1 2a1 1 0 0 1 1-1z" fill="#1e9ad6"/></svg>(555) 014-2270</li>
        <li><svg width="14" height="10" viewBox="0 0 14 10"><rect x=".5" y=".5" width="13" height="9" fill="none" stroke="#1e9ad6"/><path d="M.5 .5 7 6l6.5-5.5" fill="none" stroke="#1e9ad6"/></svg>info@trelmondgroup.com</li>
        <li><svg width="12" height="14" viewBox="0 0 12 14"><path d="M6 13S1 8 1 5a5 5 0 0 1 10 0c0 3-5 8-5 8z" fill="#1e9ad6"/><circle cx="6" cy="5" r="1.8" fill="#071a2c"/></svg>1420 Linden Street, Suite 8<br>Maple Grove, GA 30000</li>
      </ul>
    </div>
    <div>
      <h4>Get In touch</h4><div class="rule"></div>
      <div class="form"><i></i><i></i><i></i><i></i><i class="wide"></i><span class="btn btn-fill">Submit</span></div>
    </div>
  </div>
  <div class="copyright"><div class="wrap"><span>Copyright &copy; 2024 Trelmond LLC. All Rights Reserved.</span><span>Privacy Policy</span></div></div>
</footer>

</body>
</html>
```